Stationery Design Project

We need a stationary design for a well-known architect in Guadalajara, Mexico. This architect specializes in very luxurious homes and commercial developments. His clients are very sophisticated, so the letterhead should be equally sophisticated. References to mythology, etc. might be a plus. The letterhead may be embossed and will be printed on a heavy-weight linen. His homes and developments are very luxurious but not necessarily ultra-modern in their aesthetic.
Target Market(s)
High end developers and luxury home buyers
Industry/Entity Type
Architect
Look and feel

```html
<!DOCTYPE html>
<html lang="es">
<head>
<meta charset="utf-8">
<title>Tomás Villarreal — Arquitecto · Letterhead</title>
<link rel="stylesheet" href="https://fonts.googleapis.com/css2?family=Marcellus&family=Arimo&display=swap">
<style>
  :root {
    --paper: #ffffff;
    --ink: #000000;
  }
  html, body {
    margin: 0;
    padding: 0;
    background: var(--paper);
    overflow: hidden;
  }
  .letterhead {
    position: relative;
    width: 927px;
    height: 1200px;
    background: var(--paper);
    color: var(--ink);
    overflow: hidden;
  }
  .masthead-rule {
    position: absolute;
    left: 172px;
    top: 60px;
    width: 570px;
    height: 40px;
  }
  .masthead-name {
    position: absolute;
    left: 0;
    top: 56px;
    width: 927px;
    text-align: center;
    margin: 0;
    font-family: "Marcellus", serif;
    font-weight: 400;
    font-size: 38px;
    line-height: 44px;
    letter-spacing: 0.5px;
  }
  .masthead-name span {
    background: var(--paper);
    padding: 0 8px;
  }
  .masthead-title {
    position: absolute;
    left: 0;
    top: 102px;
    width: 902px;
    text-align: center;
    margin: 0;
    font-family: "Marcellus", serif;
    font-size: 26px;
    line-height: 30px;
  }
  .contact-block {
    position: absolute;
    left: 0;
    top: 1039px;
    width: 918px;
    text-align: center;
    font-family: "Arimo", Arial, sans-serif;
    font-size: 14px;
    line-height: 17px;
    font-style: normal;
  }
  .contact-block .web {
    margin-left: 22px;
  }
</style>
</head>
<body>
  <main class="letterhead">
    <header>
      <svg class="masthead-rule" viewBox="0 0 570 40" aria-hidden="true">
        <line x1="0" y1="17" x2="570" y2="26" stroke="var(--ink)" stroke-width="2.5"/>
      </svg>
      <h1 class="masthead-name"><span>Tomás Villarreal</span></h1>
      <p class="masthead-title">Arquitecto</p>
    </header>
    <address class="contact-block">
      Paseo de los Robles #1450<br>
      Colinas del Bosque, Zapopan<br>
      Jalisco 45110&nbsp; Mexico<br>
      (52) 33 12 58 47 90<span class="web">http://tomasvillarrealdesigns.com/</span>
    </address>
  </main>
</body>
</html>
```